Awesome photographers card for an awesome new business

Double sided business card Black background and silver logo in middle on one side. Details on otherside. please keep it simple

Photographer

Gavin Tolley
0482615073
GavinTolleyPhotography82@lumenpost.com
www.GavinTolleyPhotography.com.au
Instagram _Gavin_tolley

Requirements
Must have
• My logo in Silver
• please use instagram logo instead of "Instagram"

```html
<!DOCTYPE html>
<html lang="en">
<head>
<meta charset="utf-8">
<title>Gavin Tolley Photography – Business Card</title>
<link href="https://fonts.googleapis.com/css2?family=Montserrat:wght@400;600&display=swap" rel="stylesheet">
<style>
  :root {
    --backdrop: #3b3b3d;
    --card: #141415;
    --silver: #d9d9dc;
    --text: #e9e9ea;
    --faint: #2b2b2d;
    --rule: #bdbdc0;
  }
  * { margin: 0; padding: 0; box-sizing: border-box; }
  html, body { width: 801px; height: 1200px; overflow: hidden; background: var(--backdrop); }
  body {
    font-family: "Montserrat", sans-serif;
    display: flex; flex-direction: column; align-items: center; justify-content: space-around;
    padding: 90px 0;
  }
  .card {
    position: relative;
    width: 640px; height: 366px;
    background: var(--card);
    border-radius: 4px;
    box-shadow: 0 12px 30px rgba(0,0,0,.45);
    overflow: hidden;
  }
  /* Front */
  .brand-mark {
    position: absolute; left: 50%; top: 50%;
    width: 200px; height: 200px; transform: translate(-50%, -50%);
    border: 4px solid var(--silver); border-radius: 50%;
    display: flex; flex-direction: column; align-items: center; justify-content: center;
    color: var(--silver); font-weight: 600; text-align: center;
    letter-spacing: 3px;
  }
  .brand-mark .brand-name { font-size: 22px; line-height: 1.25; text-transform: uppercase; }
  .brand-mark .brand-sub { font-size: 10px; letter-spacing: 4px; margin-top: 8px; text-transform: uppercase; }
  /* Back */
  .backdrop-name {
    position: absolute; left: -10px; top: 40px;
    font-size: 120px; font-weight: 600; line-height: .9;
    color: var(--faint); letter-spacing: -2px;
  }
  .holder-name {
    position: absolute; left: 40px; top: 150px;
    color: var(--text); font-weight: 600; font-size: 15px; letter-spacing: .5px;
    text-transform: uppercase;
  }
  .divider {
    position: absolute; left: 232px; top: 110px; width: 1px; height: 110px; background: var(--rule);
  }
  .contact-list {
    position: absolute; left: 250px; top: 118px; list-style: none;
    color: var(--text); font-size: 13.5px; line-height: 1;
  }
  .contact-list li { display: flex; align-items: center; gap: 9px; height: 20px; }
  .contact-list svg { width: 13px; height: 13px; flex: none; fill: none; stroke: var(--text); stroke-width: 1.6; }
  .contact-list .social-dot { width: 12px; height: 12px; border-radius: 50%; background: var(--text); flex: none; }
</style>
</head>
<body>
  <section class="card card-front">
    <div class="brand-mark">
      <span class="brand-name">Gavin<br>Tolley</span>
      <span class="brand-sub">Photography</span>
    </div>
  </section>

  <section class="card card-back">
    <div class="backdrop-name" aria-hidden="true">Gavin<br>Tolley</div>
    <p class="holder-name">Gavin Tolley</p>
    <div class="divider"></div>
    <ul class="contact-list">
      <li>
        <svg viewBox="0 0 16 16"><path d="M3 2h3l1.5 3.5-2 1.2a8 8 0 0 0 3.8 3.8l1.2-2L14 10v3a1 1 0 0 1-1 1A11 11 0 0 1 2 3a1 1 0 0 1 1-1z"/></svg>
        0482 615 073
      </li>
      <li>
        <svg viewBox="0 0 16 16"><rect x="1.5" y="3.5" width="13" height="9" rx="1"/><path d="M1.5 4l6.5 5 6.5-5"/></svg>
        GavinTolleyPhotography82@lumenpost.com
      </li>
      <li>
        <svg viewBox="0 0 16 16"><circle cx="8" cy="8" r="6.5"/><path d="M1.5 8h13M8 1.5c-3 3.5-3 9.5 0 13M8 1.5c3 3.5 3 9.5 0 13"/></svg>
        www.GavinTolleyPhotography.com.au
      </li>
      <li>
        <span class="social-dot" aria-hidden="true"></span>
        _Gavin_tolley
      </li>
    </ul>
  </section>
</body>
</html>
```